Adwords Banner for unique handmade Jewelery

We need one Banner for our Jewelerys
in 4 sizes:
300x250px
336x280px
728x90px
160x600px

http://www.torvik-mela.de/schmuck/2/

```html
<!DOCTYPE html>
<html lang="de">
<head>
<meta charset="utf-8">
<title>torvik mela – Banner</title>
<link rel="stylesheet" href="https://fonts.googleapis.com/css2?family=Lobster+Two:ital,wght@1,700&family=Noto+Serif:wght@400&display=swap">
<style>
  :root {
    --stage-center: #b87986;
    --stage-edge: #94505f;
    --brand-rose: #b84d68;
    --brand-rose-dark: #a53f5a;
    --headline: #c0506b;
    --copy: #b0455f;
    --card-top: #ffffff;
    --card-bottom: #e4e4e4;
    --card-border: #f3e4e8;
    --photo-light: #f4f4f4;
    --photo-mid: #e3d3d8;
    --photo-accent: #d88a9d;
    --button-top: #d7738c;
    --button-bottom: #ad3f5b;
    --white: #ffffff;
  }

  * { margin: 0; padding: 0; box-sizing: border-box; }

  html, body {
    width: 1200px;
    height: 690px;
    overflow: hidden;
  }

  body {
    position: relative;
    background: radial-gradient(ellipse at 50% 40%, var(--stage-center) 0%, var(--stage-edge) 85%);
    font-family: "Noto Serif", Georgia, serif;
  }

  .banner {
    position: absolute;
    background: linear-gradient(180deg, var(--card-top) 0%, var(--card-bottom) 100%);
    border: 1px solid var(--card-border);
    border-radius: 11px;
    overflow: hidden;
    box-shadow: 0 2px 8px rgba(80, 20, 35, 0.25);
  }

  .brand-panel {
    position: absolute;
    background: linear-gradient(180deg, var(--brand-rose) 0%, var(--brand-rose-dark) 100%);
    display: flex;
    align-items: center;
    justify-content: center;
    gap: 10px;
  }

  .brand-name {
    color: var(--white);
    font-family: "Noto Serif", Georgia, serif;
    font-weight: 400;
    font-size: 30px;
    letter-spacing: 0.5px;
    white-space: nowrap;
  }

  .brand-dot {
    width: 12px;
    height: 12px;
    border-radius: 50%;
    background: var(--white);
  }

  .headline {
    position: absolute;
    font-family: "Lobster Two", cursive;
    font-style: italic;
    font-weight: 700;
    color: var(--headline);
    white-space: nowrap;
  }

  .product-photo {
    position: absolute;
    border-radius: 6px;
    background: radial-gradient(ellipse at 50% 55%, var(--photo-accent) 0%, var(--photo-mid) 40%, var(--photo-light) 80%);
  }

  .tagline {
    position: absolute;
    color: var(--copy);
    font-size: 16.5px;
    line-height: 1.2;
  }

  .cta {
    position: absolute;
    display: flex;
    align-items: center;
    justify-content: center;
    gap: 8px;
    border-radius: 17px;
    background: linear-gradient(180deg, var(--button-top) 0%, var(--button-bottom) 100%);
    color: var(--white);
    font-size: 17px;
    text-decoration: none;
    box-shadow: 0 1px 2px rgba(80, 20, 35, 0.35);
  }

  .cta svg { display: block; }

  /* medium rectangle */
  .banner--rect { left: 421px; top: 77px; width: 358px; height: 357px; }
  .banner--rect .brand-panel { left: 0; top: 0; width: 100%; height: 80px; }
  .banner--rect .headline { left: 0; width: 100%; text-align: center; top: 98px; font-size: 29px; }
  .banner--rect .product-photo { left: 20px; top: 143px; width: 318px; height: 122px; }
  .banner--rect .tagline { left: 18px; top: 275px; width: 160px; }
  .banner--rect .cta { left: 176px; top: 298px; width: 158px; height: 34px; }

  /* leaderboard */
  .banner--wide { left: 78px; top: 485px; width: 1038px; height: 129px; }
  .banner--wide .brand-panel { left: 0; top: 0; width: 263px; height: 100%; }
  .banner--wide .product-photo { left: 289px; top: 10px; width: 301px; height: 109px; }
  .banner--wide .headline { left: 607px; top: 13px; font-size: 34px; }
  .banner--wide .tagline { left: 607px; top: 68px; width: 240px; }
  .banner--wide .cta { left: 858px; top: 74px; width: 157px; height: 34px; }
</style>
</head>
<body>

  <section class="banner banner--rect" aria-label="Banner 300 x 250">
    <div class="brand-panel">
      <span class="brand-dot"></span>
      <span class="brand-name">torvik mela</span>
    </div>
    <h2 class="headline">Einzigartig: Der Schmuck</h2>
    <div class="product-photo" role="img" aria-label="Produktfoto: Armband mit rosa Glasperlen und Silberkugeln"></div>
    <p class="tagline">hochwertigen und handgefertigten Schmucks</p>
    <a class="cta" href="http://www.torvik-mela.de/schmuck/2/">
      jetzt kaufen
      <svg width="14" height="14" viewBox="0 0 14 14" aria-hidden="true">
        <circle cx="7" cy="7" r="7" fill="#ffffff"/>
        <path d="M5.5 4 L9.5 7 L5.5 10 Z" fill="#ad3f5b"/>
      </svg>
    </a>
  </section>

  <section class="banner banner--wide" aria-label="Banner 728 x 90">
    <div class="brand-panel">
      <span class="brand-dot"></span>
      <span class="brand-name">torvik mela</span>
    </div>
    <div class="product-photo" role="img" aria-label="Produktfoto: Armband mit rosa Glasperlen und Silberkugeln"></div>
    <h2 class="headline">Einzigartig: Der Schmuck</h2>
    <p class="tagline">hochwertigen und handgefertigten Schmucks</p>
    <a class="cta" href="http://www.torvik-mela.de/schmuck/2/">
      jetzt kaufen
      <svg width="14" height="14" viewBox="0 0 14 14" aria-hidden="true">
        <circle cx="7" cy="7" r="7" fill="#ffffff"/>
        <path d="M5.5 4 L9.5 7 L5.5 10 Z" fill="#ad3f5b"/>
      </svg>
    </a>
  </section>

</body>
</html>
```